Property casualty insurance consultant. Review business insurance plans and provide risk mgmt advice

Front side: logo, tag line, name and info
Back side: Services

Front:
Marcus T. Dole
Property / Casualty Insurance Consulting and Training
P.O. Box 7386
Greensboro, NC 27519
marcus@brightfenpartners.example 336-555-0147 www.brightfenpartners.example
Back side:
Insurance Program Review
Renewal Proposal Review
Safety Planning / Loss Control
Disaster Planning
Claims Assistance
Updates

Images uploaded. I am non tech so let me know if this did not work. Choose image with Blue Fonts and Orange design element. The brief has also changed to put all info on front and services on back. Thank you.

Reason: took a while to get images downloaded

Going through elimination process. Thanks to all. On any revisions, please add two more services on reverse: Company Training . Agency Training

Target Market(s)

Business owners of all sizes and types

Industry/Entity Type

Insurance

Requirements
Must have
• Logo will have the colors to use, info fonts probably black and should closely match that in logo. Front side, logo, tag line, name and info. Back side with services and logo design element incorporated somehow

```html
<!DOCTYPE html>
<html lang="en">
<head>
<meta charset="utf-8">
<title>Brightfen Partners – Business Cards</title>
<link rel="stylesheet" href="https://fonts.googleapis.com/css2?family=Questrial&display=swap">
<style>
  :root {
    --backdrop: #d9d9d7;
    --card-black: #121212;
    --brand-white: #f4f4f4;
    --accent-red: #b43a3a;
    --detail-white: #e6e6e6;
    --tagline-grey: #9a9a9a;
    --card-shadow: rgba(0, 0, 0, 0.28);
  }

  * { box-sizing: border-box; margin: 0; padding: 0; }

  html, body {
    width: 1200px;
    height: 1200px;
    overflow: hidden;
    background: var(--backdrop);
    font-family: "Questrial", "Century Gothic", sans-serif;
  }

  .sheet {
    position: relative;
    width: 1200px;
    height: 1200px;
  }

  .card {
    position: absolute;
    left: 220px;
    width: 760px;
    height: 434px;
    background: var(--card-black);
    box-shadow: 0 14px 30px var(--card-shadow);
    color: var(--brand-white);
  }

  .card--front { top: 130px; }
  .card--back  { top: 636px; }

  .brand-name {
    position: absolute;
    font-size: 44px;
    line-height: 1;
    letter-spacing: 0.5px;
    color: var(--brand-white);
    white-space: nowrap;
  }

  .card--front .brand-name {
    left: 62px;
    top: 58px;
  }

  .card--back .brand-name {
    left: 0;
    right: 0;
    top: 62px;
    text-align: center;
  }

  .holder-name {
    color: var(--accent-red);
    font-size: 30px;
    letter-spacing: 0.6px;
    white-space: nowrap;
  }

  .contact-block {
    position: absolute;
    left: 400px;
    top: 196px;
  }

  .contact-block .holder-name { margin-bottom: 14px; }

  .contact-lines {
    list-style: none;
    font-size: 15px;
    line-height: 26px;
    color: var(--detail-white);
    letter-spacing: 0.3px;
    white-space: nowrap;
  }

  .service-list {
    position: absolute;
    left: 90px;
    right: 90px;
    top: 158px;
    list-style: none;
    display: grid;
    grid-template-columns: 1fr 1fr;
    column-gap: 40px;
    row-gap: 12px;
    font-size: 18px;
    line-height: 24px;
    color: var(--detail-white);
    letter-spacing: 0.3px;
    white-space: nowrap;
  }

  .service-list li::before {
    content: "";
    display: inline-block;
    width: 7px;
    height: 7px;
    margin-right: 12px;
    vertical-align: middle;
    background: var(--accent-red);
  }

  .tagline {
    position: absolute;
    left: 0;
    right: 0;
    top: 346px;
    text-align: center;
    font-size: 19px;
    color: var(--tagline-grey);
    letter-spacing: 0.4px;
    white-space: nowrap;
  }
</style>
</head>
<body>
  <main class="sheet">
    <section class="card card--front" aria-label="Front of business card with contact details">
      <p class="brand-name">Brightfen Partners</p>
      <div class="contact-block">
        <p class="holder-name">Marcus T. Dole</p>
        <ul class="contact-lines">
          <li>P.O. Box 7386</li>
          <li>Greensboro, NC 27519</li>
          <li>marcus@brightfenpartners.example</li>
          <li>phone 336-555-0147</li>
          <li>www.brightfenpartners.example</li>
        </ul>
      </div>
    </section>

    <section class="card card--back" aria-label="Back of business card with services">
      <p class="brand-name">Brightfen Partners</p>
      <ul class="service-list">
        <li>Insurance Program Review</li>
        <li>Disaster Planning</li>
        <li>Renewal Proposal Review</li>
        <li>Claims Assistance</li>
        <li>Safety Planning / Loss Control</li>
        <li>Updates</li>
        <li>Company Training</li>
        <li>Agency Training</li>
      </ul>
      <p class="tagline">Property / Casualty Insurance Consulting and Training</p>
    </section>
  </main>
</body>
</html>
```